Letterhead & Business Card for our Professional Practice (Financial Services)

We are looking for someone to design a letterhead and business card for our business, which is a professional practice called Corvel Brook Capital Limited. The website is at www.corvelbrookcapitel.example.

The letterhead needs to have: (a) our logo (b) address (c) telephone number (d) email address and (e) our company number.

We would like the stationary to be consistent with the website.

I have attached the logo in EPS and PNG format.

Target Market(s)

Professional services, large commercial enterprises, financial services

Industry/Entity Type

Financial Service

Font styles to use
Serif

Colors
3176b5
f04a50

Requirements
Must have
• Be consistent with our website located at www.corvelbrookcapital.example
• Be in the following formats:
• 1. Word template for the letterhead
• 2. PDF for the letterhead with setup and bleeds required at www.presslyne88.example
• 3. PDF for the business card with setup and bleeds required at www.presslyne88.example
Nice to have
• Something with a really interesting design that says "these guys are professional but dynamic and interesting"
Should not have
• Boring

```html
<!DOCTYPE html>
<html lang="en">
<head>
<meta charset="utf-8">
<title>Corvel Brook Capital — Stationery</title>
<link href="https://fonts.googleapis.com/css2?family=Open+Sans:wght@400;600&display=swap" rel="stylesheet">
<style>
  :root {
    --navy: #183e70;
    --red: #d21f30;
    --ink-grey: #6d6d6d;
    --paper: #ffffff;
    --backdrop: #b09c80;
  }
  * { margin: 0; padding: 0; box-sizing: border-box; }
  html, body { width: 1200px; height: 1110px; overflow: hidden; }
  body {
    position: relative;
    background: var(--backdrop);
    font-family: "Open Sans", Arial, sans-serif;
  }

  .brand {
    position: absolute; display: flex; align-items: center; gap: 6px;
    color: var(--navy); font-weight: 600; white-space: nowrap;
  }
  .brand__square { background: var(--red); flex: none; }

  /* Letterhead */
  .letterhead {
    position: absolute; left: 317px; top: 186px;
    width: 511px; height: 705px;
    background: var(--paper);
    overflow: hidden;
  }
  .letterhead__shapes { position: absolute; inset: 0; }
  .letterhead__masthead {
    position: absolute; left: 33px; top: 74px; width: 420px;
    display: flex; align-items: flex-end; gap: 4px;
  }
  .letterhead__masthead .brand { position: static; font-size: 16px; line-height: 20px; }
  .letterhead__masthead .brand__square { width: 12px; height: 12px; }
  .letterhead__rule {
    flex: 1; height: 1px; margin-bottom: 3px;
    background: var(--red);
  }
  .letterhead__address {
    position: absolute; right: 58px; top: 39px;
    font-size: 9px; line-height: 11px; text-align: right; color: var(--ink-grey);
    font-style: normal;
  }
  .footer-band { position: absolute; top: 646px; height: 3px; }
  .footer-band--red { left: 0; width: 180px; background: var(--red); }
  .footer-band--navy { left: 180px; width: 331px; background: var(--navy); }
  .letterhead__web {
    position: absolute; left: 34px; top: 657px;
    font-size: 10px; color: var(--navy);
  }
  .contact { position: absolute; top: 653px; font-size: 6.5px; line-height: 8px; color: var(--ink-grey); }
  .contact svg { display: block; margin-bottom: 2px; }
  .contact--phone { left: 299px; }
  .contact--mail { left: 393px; }
  .contact__divider {
    position: absolute; left: 386px; top: 655px; width: 1px; height: 38px;
    background: #9a9a9a;
  }

  /* Business cards */
  .card {
    position: absolute; left: 873px; width: 196px; height: 133px; overflow: hidden;
  }
  .card svg.card__bg { position: absolute; inset: 0; }
  .card--front { top: 329px; }
  .card--back { top: 493px; }
  .card--front .brand { left: 34px; top: 44px; font-size: 8.5px; gap: 4px; }
  .card--front .brand__square { width: 7px; height: 7px; }
  .card__person { position: absolute; left: 16px; top: 62px; }
  .card__name { font-size: 7px; font-weight: 600; color: #222; }
  .card__role { font-size: 5px; color: var(--ink-grey); }
  .card__lines { position: absolute; left: 16px; top: 81px; font-size: 4.2px; line-height: 6px; color: var(--navy); }
  .card__lines span::before {
    content: ""; display: inline-block; width: 3.5px; height: 3.5px; margin-right: 2px;
    border: 0.7px solid var(--red); border-radius: 1px; vertical-align: -0.5px;
  }
  .card__address {
    position: absolute; right: 16px; top: 88px; font-size: 4.6px; line-height: 6px;
    color: #fff; text-align: right;
  }
  .card__address svg { display: block; margin: 0 0 2px auto; }
  .card--back .brand { left: 36px; top: 62px; font-size: 11px; gap: 5px; }
  .card--back .brand__square { width: 8px; height: 8px; }
  .card__web {
    position: absolute; left: 0; right: 0; top: 80px; padding-left: 22px;
    text-align: center; font-size: 5.5px; font-weight: 600; color: var(--red);
  }
</style>
</head>
<body>

<section class="letterhead" aria-label="Letterhead">
  <svg class="letterhead__shapes" width="511" height="705" viewBox="0 0 511 705" aria-hidden="true">
    <defs>
      <linearGradient id="ghostFade" x1="0" y1="0" x2="1" y2="1">
        <stop offset="0" stop-color="#f6f6f7"/>
        <stop offset="1" stop-color="#e9e9eb"/>
      </linearGradient>
      <linearGradient id="leftFade" x1="0" y1="0" x2="1" y2="0">
        <stop offset="0" stop-color="#f7f7f8"/>
        <stop offset="1" stop-color="#f1f1f3"/>
      </linearGradient>
    </defs>
    <path d="M511 215 L511 705 L260 705 L250 610 Q225 560 260 515 Z" fill="url(#ghostFade)" opacity="0.7"/>
    <path d="M0 375 L360 515 Q395 530 385 575 L375 646 L0 646 Z" fill="url(#leftFade)" opacity="0.8"/>
    <path d="M260 515 Q300 500 360 515 Q395 530 385 575 Q370 615 320 620 Q255 620 235 590 Q222 545 260 515 Z" fill="#e9e9ec"/>
    <rect x="0" y="648" width="511" height="57" fill="#f7f7f8"/>
  </svg>

  <div class="letterhead__masthead">
    <div class="brand"><span class="brand__square"></span>Corvel Brook Capital</div>
    <div class="letterhead__rule"></div>
  </div>
  <address class="letterhead__address">
    14-16 Harlow Quay<br>Fenmouth,<br>Wessex,<br>FM2 7QD
  </address>

  <div class="footer-band footer-band--red"></div>
  <div class="footer-band footer-band--navy"></div>
  <div class="letterhead__web">www.corvelbrookcapital.example</div>

  <div class="contact contact--phone">
    <svg width="14" height="12" viewBox="0 0 14 12" aria-hidden="true">
      <path d="M3 1 L5 1 L6 4 L4.5 5 Q6 8 9 9 L10 7.5 L13 8.5 L13 10.5 Q12 11.5 10 11 Q3 9 2 2.5 Q2 1.2 3 1 Z" fill="none" stroke="var(--red)" stroke-width="1"/>
    </svg>
    01632 960418<br>Working Monday - Friday<br>8am - 5pm
  </div>
  <div class="contact__divider"></div>
  <div class="contact contact--mail">
    <svg width="14" height="11" viewBox="0 0 14 11" aria-hidden="true">
      <rect x="1" y="1" width="12" height="9" fill="none" stroke="var(--red)" stroke-width="1"/>
      <path d="M1 1 L7 6 L13 1" fill="none" stroke="var(--red)" stroke-width="1"/>
    </svg>
    contact@corvelbrookcapital.example
  </div>
</section>

<section class="card card--front" aria-label="Business card, front">
  <svg class="card__bg" width="196" height="133" viewBox="0 0 196 133" aria-hidden="true">
    <rect width="196" height="133" fill="var(--navy)"/>
    <path d="M4 0 L176 0 Q196 2 186 16 L66 133 L20 133 Z" fill="#fff"/>
  </svg>
  <div class="brand"><span class="brand__square"></span>Corvel Brook Capital</div>
  <div class="card__person">
    <div class="card__name">Name Surname</div>
    <div class="card__role">Designation</div>
  </div>
  <div class="card__lines">
    <span>01632 960418</span><br>
    <span>contact@corvelbrookcapital.example</span><br>
    <span>www.corvelbrookcapital.example</span>
  </div>
  <div class="card__address">
    <svg width="5" height="7" viewBox="0 0 5 7" aria-hidden="true">
      <path d="M2.5 7 L0.6 3.4 A2 2 0 1 1 4.4 3.4 Z" fill="none" stroke="#fff" stroke-width="0.6"/>
    </svg>
    14-16 Harlow Quay<br>Fenmouth, Wessex, FM2 7QD
  </div>
</section>

<section class="card card--back" aria-label="Business card, back">
  <svg class="card__bg" width="196" height="133" viewBox="0 0 196 133" aria-hidden="true">
    <rect width="196" height="133" fill="var(--red)"/>
    <path d="M28 0 L190 0 L160 133 L96 133 L6 40 Q-4 26 10 10 Q18 0 28 0 Z" fill="#fff"/>
  </svg>
  <div class="brand"><span class="brand__square"></span>Corvel Brook Capital</div>
  <div class="card__web">www.corvelbrookcapital.example</div>
</section>

</body>
</html>
```